Wordpress Design Project

Hello Happy People,

My name is Tav i run a company called brightpathco.net.au am working on a new project with LED lighting and have decided to try pixel forum as i've heard great things.

Our company is in need of wordpress design for a new company 'glow orb' we are a distribution and sales company dealing with the best LED lighting products in the world :)

We are targeting commercial customers, small and medium also!

I would like a wordpress design based on the logos, pictures and content that i provide.

home page
distributor
lighting school
small medium enterprise
commercial enterprise
industrial and mining
product categories (30 products)
contact us

We will be on linkedin & facebook

Our company website is www.gloworb.com.au and www.vextra.com.au

I am available for the next 10 days to go through with anyone that is interested in taking this project on and will offer work

Requirements
Must have
• i would like the website to follow the design logo i have created originally

```html
<!DOCTYPE html>
<html lang="en">
<head>
<meta charset="utf-8">
<title>glow orb — LED lighting</title>
<link rel="stylesheet" href="https://fonts.googleapis.com/css2?family=Jost:wght@400;500;600&family=Arimo:wght@400;700&display=swap">
<style>
:root{
  --bg-dark:#23272a;
  --page:#ffffff;
  --ink:#222222;
  --ink-soft:#4a4a48;
  --muted:#8c8c8c;
  --accent:#eea91a;
  --nav-top:#5a5854;
  --nav-bottom:#2a2926;
  --rule:#e2e2e2;
}
*{box-sizing:border-box;margin:0;padding:0}
html,body{width:1200px;height:1069px;overflow:hidden}
body{background:var(--bg-dark);font-family:"Arimo",Arial,sans-serif;font-size:10.1px;color:var(--ink);position:relative}
.page{position:absolute;left:177px;top:15px;width:845px;height:1037px;border-radius:24px;border:3px solid #f4f4f4;overflow:hidden;
  background:linear-gradient(#ebebeb 0,#ffffff 110px,#ffffff 100%)}
.abs{position:absolute}
.brand{left:17px;top:31px;display:flex;align-items:center;gap:10px}
.brand-mark{width:54px;height:54px;border-radius:50%;border:5px solid var(--accent);flex:none}
.brand-name{font-family:"Jost",sans-serif;font-weight:600;font-size:40px;color:var(--ink-soft);letter-spacing:-1px;white-space:nowrap}
.search{left:619px;top:51px;width:211px;height:25px;border:1px solid #cfcfcf;border-top-color:#b5b5b5;background:linear-gradient(#e2e2e2,#f7f7f7);display:flex;align-items:center;justify-content:space-between;padding:0 8px 0 10px;font-size:10.5px;color:#666}
.nav{left:3px;top:107px;width:833px;height:49px;border-radius:10px;border:1px solid #1e1d1b;background:linear-gradient(var(--nav-top),var(--nav-bottom));display:flex;overflow:hidden}
.nav a{color:#fff;text-decoration:none;font-family:"Jost",sans-serif;font-size:15.5px;display:flex;align-items:center;justify-content:center;border-right:1px solid #1f1e1c;box-shadow:1px 0 0 #55534f}
.nav a:last-child{border:none;box-shadow:none}
.hero{left:3px;top:165px;width:833px;height:303px;border:1px solid #d8d8d8;border-radius:10px;background:#fff;overflow:hidden}
.hero h1{position:absolute;left:47px;top:50px;font-family:"Jost",sans-serif;font-weight:500;font-size:22px;line-height:31px;color:var(--ink-soft);letter-spacing:.3px;white-space:nowrap}
.hero h1 span{color:var(--accent);display:block}
.hero p{position:absolute;left:47px;top:132px;width:264px;font-size:10.1px;line-height:19.4px;text-align:justify;color:var(--ink)}
.btn{position:absolute;left:47px;top:206px;width:81px;height:30px;border-radius:12px;background:linear-gradient(#5a5856,#2c2b29);color:#fff;font-family:"Jost",sans-serif;font-size:11px;display:flex;align-items:center;justify-content:center;border:1px solid #1a1a1a}
.dots{position:absolute;left:54px;top:252px;display:flex;gap:2px}
.dots i{width:14px;height:14px;border-radius:50%;border:2px solid #d2d2d2;background:#fafafa;display:block}
.dots i.on{background:var(--accent);border-color:#c98a08}
.hero-photo{position:absolute;left:323px;top:0;width:510px;height:303px;background:radial-gradient(ellipse at 55% 50%,#c9c9c9 0,#e8e8e8 45%,#ffffff 75%)}
h2{font-family:"Jost",sans-serif;font-weight:400;font-size:17.7px;color:var(--ink-soft);white-space:nowrap}
.welcome-band{left:3px;top:476px;width:833px;height:70px;background:linear-gradient(#f0f0f0,#fff)}
.welcome-title{left:17px;top:484px}
.welcome-photo{left:17px;top:526px;width:184px;height:154px;border-radius:10px;border:1px solid #ccc;background:linear-gradient(#0b0d12 0,#1d2430 55%,#3a2a22 85%,#120f0f 100%)}
.welcome-text{left:214px;top:525px;width:620px;line-height:15.2px;text-align:justify}
.welcome-text b{display:block;margin-bottom:15px}
a.more{color:var(--accent);font-size:10.1px;text-decoration:underline}
.rule-h{height:1px;background:var(--rule)}
.col-rule{left:531px;top:718px;width:1px;height:209px;background:var(--rule)}
.services-title{left:17px;top:717px}
.services-intro{left:17px;top:754px;width:484px;line-height:15.2px;text-align:justify}
.service-list{left:40px;top:808px;width:480px;display:grid;grid-template-columns:252px 228px;row-gap:13px;list-style:none}
.service-list li{display:flex;align-items:center;gap:9px;height:13px;white-space:nowrap}
.tick{width:8px;height:8px;flex:none}
.news-title{left:552px;top:717px}
.news{left:552px;width:275px;line-height:15.2px}
.news .date{color:var(--accent);font-weight:700;margin-bottom:3px}
.footer{left:3px;top:945px;width:833px;height:92px;background:linear-gradient(#ffffff,#dcdcdc)}
.foot-brand{left:25px;top:970px;display:flex;align-items:center;gap:7px}
.foot-brand .brand-mark{width:42px;height:42px;border:4px solid #a8a8a8}
.foot-brand .brand-name{font-size:28px;color:#9c9c9c}
.foot-sep{top:965px;width:1px;height:62px;background:#d4d4d4}
.foot-contact{left:218px;top:964px;line-height:15.2px;color:var(--muted);white-space:nowrap}
.foot-links{left:403px;top:964px;line-height:15.2px;color:var(--muted);white-space:nowrap}
.foot-links span{color:var(--ink)}
.social{left:403px;top:1001px;display:flex;gap:9px}
.social i{width:24px;height:24px;border-radius:3px;background:linear-gradient(#8a8a8a,#5d5d5d);display:block}
</style>
</head>
<body>
<div class="page">
  <div class="abs brand"><span class="brand-mark"></span><span class="brand-name">glow orb</span></div>
  <div class="abs search">Search...
    <svg width="13" height="13" viewBox="0 0 13 13"><circle cx="5" cy="5" r="3.8" fill="none" stroke="#777" stroke-width="1.6"/><line x1="8" y1="8" x2="12" y2="12" stroke="#777" stroke-width="2"/></svg>
  </div>
  <nav class="abs nav">
    <a href="#" style="width:100px">Home</a>
    <a href="#" style="width:104px">About Us</a>
    <a href="#" style="width:131px">Our Products</a>
    <a href="#" style="width:101px">Services</a>
    <a href="#" style="width:121px">Technology</a>
    <a href="#" style="width:167px">Lighting Solutions</a>
    <a href="#" style="width:109px">Contact</a>
  </nav>
  <section class="abs hero">
    <div class="hero-photo" role="img" aria-label="Assortment of LED bulbs and spotlights on a white reflective surface"></div>
    <h1>SAVING ENERGY THROUGH <span>LED TECHNOLOGY</span></h1>
    <p>Vestibulum mattis vulputate mattis. Suspendisse facilisis, eros sit amet eleifend mollis, risus dui dapibus justo, id dapibus nisi metus quis quam. In hac habitasse platea dictumst. Proin tincidunt condimentum faucibus.</p>
    <div class="btn">Read more</div>
    <div class="dots"><i class="on"></i><i></i><i></i><i></i></div>
  </section>
  <div class="abs welcome-band"></div>
  <h2 class="abs welcome-title">Welcome to Our Glow Orb</h2>
  <div class="abs welcome-photo" role="img" aria-label="Solar powered LED street lights glowing at night above a row of trees"></div>
  <div class="abs welcome-text">
    <b>Morbi sollicitudin ultrices mauris, ac sodales sem ullamcorper a. Integer in sapien felis, eu convallis sem. Maecenas convallis varius velit eget semper. Donec eu eros a libero posuere pretium sit amet a mauris.</b>
    Ut ipsum quam, suscipit in porttitor ac, sodales quis enim. Donec cursus eros libero. Pellentesque tempus tincidunt porta. Morbi ut elementum nunc. Etiam feugiat, quam a pharetra auctor, ipsum lectus congue libero, eu semper justo dui in ante. Quisque aliquam mauris ac erat porta et vehicula arcu euismod. In eu gravida est. In ac cursus sapien. Lorem ipsum dolor sit amet, consectetur adipiscing elit. Class aptent taciti sociosqu ad litora torquent per conubia nostra, per inceptos himenaeos. Aliquam scelerisque, turpis id iaculis dignissim, justo nulla auctor lorem, sed interdum velit lorem aliquet nibh. Maecenas id sodales dolor. Pellentesque non nisi nec mi lobortis bibendum a vel diam.
  </div>
  <a class="abs more" href="#" style="left:214px;top:659px">Read more....</a>
  <div class="abs rule-h" style="left:3px;top:701px;width:833px"></div>
  <div class="abs col-rule"></div>
  <h2 class="abs services-title">Our Services</h2>
  <p class="abs services-intro">Morbi sollicitudin ultrices mauris, ac sodales sem ullamcorper a. Integer in sapien felis, eu convallis sem. Maecenas convallis varius velit eget semper.</p>
  <ul class="abs service-list">
    <li><svg class="tick" viewBox="0 0 8 8"><rect x=".5" y=".5" width="7" height="7" fill="#fff" stroke="#555"/><path d="M2 4h3M4 2.5 5.5 4 4 5.5" stroke="#555" fill="none"/></svg>Maecenas id sodales dolor.</li>
    <li><svg class="tick" viewBox="0 0 8 8"><rect x=".5" y=".5" width="7" height="7" fill="#fff" stroke="#555"/><path d="M2 4h3M4 2.5 5.5 4 4 5.5" stroke="#555" fill="none"/></svg>Morbi imperdiet ultrices est eget placerat.</li>
    <li><svg class="tick" viewBox="0 0 8 8"><rect x=".5" y=".5" width="7" height="7" fill="#fff" stroke="#555"/><path d="M2 4h3M4 2.5 5.5 4 4 5.5" stroke="#555" fill="none"/></svg>Pellentesque non nisi nec</li>
    <li><svg class="tick" viewBox="0 0 8 8"><rect x=".5" y=".5" width="7" height="7" fill="#fff" stroke="#555"/><path d="M2 4h3M4 2.5 5.5 4 4 5.5" stroke="#555" fill="none"/></svg>Nulla eget dui diam.</li>
    <li><svg class="tick" viewBox="0 0 8 8"><rect x=".5" y=".5" width="7" height="7" fill="#fff" stroke="#555"/><path d="M2 4h3M4 2.5 5.5 4 4 5.5" stroke="#555" fill="none"/></svg>Mi lobortis bibendum a vel diam.</li>
    <li><svg class="tick" viewBox="0 0 8 8"><rect x=".5" y=".5" width="7" height="7" fill="#fff" stroke="#555"/><path d="M2 4h3M4 2.5 5.5 4 4 5.5" stroke="#555" fill="none"/></svg>In ac tortor ipsum, vel accumsan neque.</li>
    <li><svg class="tick" viewBox="0 0 8 8"><rect x=".5" y=".5" width="7" height="7" fill="#fff" stroke="#555"/><path d="M2 4h3M4 2.5 5.5 4 4 5.5" stroke="#555" fill="none"/></svg>Quisque ultrices placerat consectetur.</li>
    <li><svg class="tick" viewBox="0 0 8 8"><rect x=".5" y=".5" width="7" height="7" fill="#fff" stroke="#555"/><path d="M2 4h3M4 2.5 5.5 4 4 5.5" stroke="#555" fill="none"/></svg>Cum sociis natoque penatibus et</li>
  </ul>
  <a class="abs more" href="#" style="left:17px;top:920px">Read more....</a>
  <h2 class="abs news-title">Latest News</h2>
  <div class="abs news" style="top:755px">
    <div class="date">DEC 31, 2012</div>
    Morbi sollicitudin ultrices mauris, ac sodales sem ullamcorper a. Integer in sapien felis, eu convallis sem. Maecenas convallis varius velit eget semper.
  </div>
  <div class="abs rule-h" style="left:552px;top:827px;width:275px"></div>
  <div class="abs news" style="top:836px">
    <div class="date">DEC 30, 2012</div>
    Morbi sollicitudin ultrices mauris, ac sodales sem ullamcorper a. Integer in sapien felis, eu convallis sem. Maecenas convallis varius velit eget semper.
  </div>
  <div class="abs rule-h" style="left:552px;top:908px;width:275px"></div>
  <a class="abs more" href="#" style="left:552px;top:920px">Read more....</a>
  <div class="abs rule-h" style="left:3px;top:945px;width:833px"></div>
  <footer class="abs footer"></footer>
  <div class="abs foot-brand"><span class="brand-mark"></span><span class="brand-name">glow orb</span></div>
  <div class="abs foot-sep" style="left:202px"></div>
  <div class="abs foot-contact">Office Phone +61 8 8000 4120<br>Mobile +61 400 555 219<br>24 Harlow Street,<br>Kensington, 5068 SA</div>
  <div class="abs foot-sep" style="left:383px"></div>
  <div class="abs foot-links">Home | About Us | Our Products | Services | Technology | Lighting Solutions | Contact Us<br>Careers | Terms of Use | Sitemap | <span>© 2012 Glow Orb. All rights reserved.</span></div>
  <div class="abs social"><i></i><i></i><i></i><i></i><i></i></div>
</div>
</body>
</html>
```